Kessel Fahrwerkstatt
Sehr angenehme zusammenarbeit nicht aufdringlich und genau auf die Wünsche eingegangen. Wir werde sicher noch mehr zusammen Arbeiten. Gruss Lukas Hemmerle Inhaber Kessel Fahrwerkstatt
Zielgruppe
Dinks und Kunden mit viel Erfolg und hohem Ausgabepotential.
Aufgabenstellung
Unsere Firma vertreibt Fahrzeuge im Luxusbereich hauptgebiet Valtro aber auch andere Sportwagen. Was uns fehlt ist ein optischer Wiedererkennugswert. Deshalb hätten wir gerne ein Visitenkarten Design und Briefpapier Design. Später soll auch noch eine Webseite mit gleichem Wiedererkennungswert entstehen. " Roter Faden "

```html
<!DOCTYPE html>
<html lang="de">
<head>
<meta charset="utf-8">
<title>Kessel Fahrwerkstatt – Visitenkarte</title>
<link href="https://fonts.googleapis.com/css2?family=Cabin:wght@400;500&display=swap" rel="stylesheet">
<style>
  :root {
    --page-bg: #e7e7e5;
    --card-light: #a0062c;
    --card-mid: #85031f;
    --card-dark: #5a0012;
    --ink: #ffffff;
    --ink-soft: #f3e4e8;
    --mark: #d9a3b0;
    --glow: rgba(222, 150, 170, 0.22);
  }
  html, body {
    margin: 0;
    padding: 0;
    width: 1200px;
    height: 910px;
    overflow: hidden;
    background: var(--page-bg);
    font-family: "Cabin", sans-serif;
  }
  .canvas {
    position: relative;
    width: 1200px;
    height: 910px;
  }
  .card {
    position: absolute;
    width: 620px;
    height: 410px;
    background: radial-gradient(ellipse 90% 85% at 45% 0%, var(--card-light) 0%, var(--card-mid) 55%, var(--card-dark) 100%);
    box-shadow: 0 6px 14px rgba(0, 0, 0, 0.28);
    overflow: hidden;
    color: var(--ink);
  }
  .card--front { left: 62px; top: 52px; }
  .card--back { left: 530px; top: 460px; }

  .card__accent {
    position: absolute;
    right: -60px;
    top: -20px;
    width: 360px;
    height: 450px;
    background: radial-gradient(ellipse 50% 50% at 55% 50%, var(--glow) 0%, rgba(222, 150, 170, 0.1) 45%, rgba(222, 150, 170, 0) 75%);
  }

  .brand {
    position: absolute;
    text-align: center;
    text-transform: uppercase;
    font-weight: 500;
    color: var(--ink);
  }
  .brand__dot {
    display: block;
    margin: 0 auto;
    border-radius: 50%;
    background: var(--mark);
  }
  .brand__name {
    display: block;
    letter-spacing: 0.02em;
  }

  .card--front .brand {
    left: 20px;
    top: 166px;
    width: 360px;
  }
  .card--front .brand__dot {
    width: 64px;
    height: 64px;
    margin-bottom: 34px;
  }
  .card--front .brand__name {
    font-size: 35px;
    line-height: 1.08;
  }

  .card--back .brand {
    left: 30px;
    top: 52px;
    width: 210px;
  }
  .card--back .brand__dot {
    width: 38px;
    height: 38px;
    margin-bottom: 20px;
  }
  .card--back .brand__name {
    font-size: 19.5px;
    line-height: 1.15;
  }

  .contact {
    position: absolute;
    left: 54px;
    top: 182px;
    font-size: 16.5px;
    line-height: 1.42;
    font-style: normal;
    color: var(--ink-soft);
  }
  .contact p { margin: 0 0 10px; }
</style>
</head>
<body>
<main class="canvas">
  <section class="card card--front" aria-label="Visitenkarte Vorderseite">
    <div class="card__accent" aria-hidden="true"></div>
    <div class="brand">
      <span class="brand__dot" aria-hidden="true"></span>
      <span class="brand__name">Kessel<br>Fahrwerkstatt</span>
    </div>
  </section>

  <section class="card card--back" aria-label="Visitenkarte Rückseite">
    <div class="card__accent" aria-hidden="true"></div>
    <div class="brand">
      <span class="brand__dot" aria-hidden="true"></span>
      <span class="brand__name">Kessel<br>Fahrwerkstatt</span>
    </div>
    <address class="contact">
      <p>Jonas Albrecht<br>Ringstr. 112 A<br>70469 Brunnfeld</p>
      <p>Tel: 0711.382 44 10<br>Fax: 0711.382 44 19</p>
      <p>E-Mail: info@kessel-fahrwerk.de<br>Web: www.kessel-fahrwerk.de</p>
    </address>
  </section>
</main>
</body>
</html>
```